Business Card Design

Hello!
We would like you to design some business cards for us. We will send you a sample of what we have. We want to take out the Tidewell Harbor Logo and add the RZD logo. This is the company that we own and it manages 7 to 8 franchised child care locations called Pebble Grove. So you can make the Pebble Grove a little logo smaller than what it currently is. Currently the back of the card lists the locations but we don't need that as we are adding new locations every few months. We can also add the website address for RZD below the logo if needed. We don't like the current design so please change it up as you like. Please let us know if you have any questions.

Industry/Entity Type

Business

Contact Information for Business Card

See above

Font styles to use
Serif
Sans Serif

Colors

Designer to choose colors to be used in the design.

Requirements
Must have
• Clean crisp look

```html
<!DOCTYPE html>
<html lang="en">
<head>
<meta charset="utf-8">
<title>RZD – Business Cards</title>
<link href="https://fonts.googleapis.com/css2?family=Arimo:wght@400;700&display=swap" rel="stylesheet">
<style>
  :root {
    --backdrop: #2b2b2b;
    --card: #f7f7f7;
    --red: #d0202e;
    --ink: #222222;
    --band: #1e1e1e;
    --band-text: #bdbdbd;
  }
  * { box-sizing: border-box; margin: 0; padding: 0; }
  html, body { width: 1200px; height: 997px; overflow: hidden; }
  body { background: var(--backdrop); position: relative; font-family: "Arimo", Arial, sans-serif; }

  .card {
    position: absolute;
    width: 620px;
    height: 355px;
    background: var(--card);
    box-shadow: 0 14px 30px rgba(0,0,0,0.55);
    overflow: hidden;
  }
  .card--front { left: 90px; top: 100px; }
  .card--back  { left: 490px; top: 520px; }

  .ruled-row {
    position: absolute; left: 40px; right: 40px;
    display: flex; align-items: center; gap: 22px;
  }
  .ruled-row__line { flex: 1; height: 1px; background: var(--red); }

  .brand { display: inline-flex; align-items: center; gap: 10px; }
  .brand__square { display: inline-block; background: var(--red); }
  .brand__name { font-weight: 700; color: var(--red); letter-spacing: 3px; line-height: 1; }

  /* front */
  .card--front .ruled-row { top: 140px; }
  .card--front .brand__square { width: 30px; height: 30px; }
  .card--front .brand__name { font-size: 46px; }
  .partner {
    position: absolute; top: 250px; left: 0; right: 0; text-align: center;
    font-size: 18px; color: var(--ink); letter-spacing: 1px;
  }

  /* back */
  .card--back .brand-top {
    position: absolute; top: 38px; left: 0; right: 0;
    display: flex; justify-content: center;
  }
  .card--back .brand__square { width: 24px; height: 24px; }
  .card--back .brand__name { font-size: 36px; }
  .card--back .ruled-row { top: 128px; }

  .contact__name { font-size: 24px; font-weight: 700; color: var(--red); letter-spacing: 0.5px; }
  .contact {
    position: absolute; top: 160px; left: 0; right: 0; text-align: center;
  }
  .contact__role { font-size: 16px; color: var(--ink); letter-spacing: 0.5px; }
  .contact__icons { display: flex; justify-content: center; gap: 14px; margin: 10px 0 6px; }
  .contact__icons svg { width: 20px; height: 20px; }
  .contact__line { font-size: 15px; color: var(--ink); line-height: 1.45; }
  .contact__web { font-size: 16px; font-weight: 700; color: var(--red); letter-spacing: 1.5px; margin-top: 2px; }

  .band {
    position: absolute; left: 0; right: 0; bottom: 0; height: 36px;
    background: var(--band); color: var(--band-text);
    font-size: 15px; display: flex; align-items: center; justify-content: center;
  }
</style>
</head>
<body>

<section class="card card--front" aria-label="Card front">
  <div class="ruled-row">
    <span class="ruled-row__line"></span>
    <div class="brand"><span class="brand__square"></span><span class="brand__name">RZD</span></div>
    <span class="ruled-row__line"></span>
  </div>
  <div class="partner">Pebble Grove</div>
</section>

<section class="card card--back" aria-label="Card back">
  <div class="brand-top">
    <div class="brand"><span class="brand__square"></span><span class="brand__name">RZD</span></div>
  </div>

  <div class="ruled-row">
    <span class="ruled-row__line"></span>
    <div class="contact__name">OMAR LENZ</div>
    <span class="ruled-row__line"></span>
  </div>

  <div class="contact">
    <div class="contact__role">ACADEMY OWNER</div>
    <div class="contact__icons">
      <svg viewBox="0 0 20 20" aria-label="Phone"><circle cx="10" cy="10" r="10" fill="#d0202e"/><rect x="5.5" y="8" width="9" height="5.5" rx="1" fill="#fff"/><rect x="7" y="5.5" width="6" height="3" rx="0.5" fill="#fff"/></svg>
      <svg viewBox="0 0 20 20" aria-label="Email"><circle cx="10" cy="10" r="10" fill="#d0202e"/><rect x="5" y="6.5" width="10" height="7" fill="#fff"/><path d="M5 6.5 L10 10.5 L15 6.5" stroke="#d0202e" stroke-width="1" fill="none"/></svg>
      <svg viewBox="0 0 20 20" aria-label="Website"><circle cx="10" cy="10" r="10" fill="#d0202e"/><path d="M8 12 L12 8" stroke="#fff" stroke-width="1.5"/><rect x="4.8" y="10.2" width="5" height="3" rx="1.5" transform="rotate(-45 7.3 11.7)" fill="none" stroke="#fff" stroke-width="1.2"/><rect x="10.2" y="6.8" width="5" height="3" rx="1.5" transform="rotate(-45 12.7 8.3)" fill="none" stroke="#fff" stroke-width="1.2"/></svg>
    </div>
    <div class="contact__line">555-014-2290</div>
    <div class="contact__line">omar.lenz@pebblegrove.net</div>
    <div class="contact__web">www.pebblegrove.net</div>
  </div>

  <div class="band">418 Larkspur Road, Suite G, Maple Falls, IL 60000</div>
</section>

</body>
</html>
```